Design some Business Cards for Torvique

I am wanting business cards designed. I will supply Logo and other details.
Needs to be simple and catch. All file formats for print must be supplied

```html
<!DOCTYPE html>
<html lang="en">
<head>
<meta charset="utf-8">
<title>Torvique Business Cards</title>
<link href="https://fonts.googleapis.com/css2?family=Open+Sans:wght@400;600;700&display=swap" rel="stylesheet">
<style>
  :root {
    --backdrop: #ecebe8;
    --card: #ffffff;
    --blue: #3fa3de;
    --blue-deep: #2b8fcf;
    --green: #7cc242;
    --ink: #2f2f2f;
    --shadow: rgba(0, 0, 0, 0.18);
  }
  * { box-sizing: border-box; margin: 0; padding: 0; }
  html, body {
    width: 1200px;
    height: 912px;
    overflow: hidden;
    background: var(--backdrop);
    font-family: "Open Sans", Arial, sans-serif;
  }
  .canvas {
    position: relative;
    width: 1200px;
    height: 912px;
  }
  .card {
    position: absolute;
    width: 560px;
    height: 320px;
    background: var(--card);
    box-shadow: 0 10px 28px var(--shadow);
    overflow: hidden;
  }
  .card-front { left: 90px; top: 100px; }
  .card-back { left: 550px; top: 490px; }

  .card-art {
    position: absolute;
    inset: 0;
    width: 100%;
    height: 100%;
  }

  .brand {
    position: absolute;
    display: flex;
    align-items: center;
    gap: 12px;
  }
  .brand-dot {
    width: 26px;
    height: 26px;
    border-radius: 50%;
    background: var(--blue);
    flex: none;
  }
  .brand-name {
    font-weight: 600;
    color: var(--blue-deep);
    letter-spacing: 0.5px;
  }
  .card-front .brand { left: 150px; top: 108px; }
  .card-front .brand-name { font-size: 44px; }
  .card-front .brand-dot { width: 34px; height: 34px; }

  .card-back .brand { right: 28px; top: 80px; gap: 8px; }
  .card-back .brand-name { font-size: 26px; }
  .card-back .brand-dot { width: 20px; height: 20px; }

  .front-web {
    position: absolute;
    right: 128px;
    bottom: 78px;
    font-size: 15px;
    font-weight: 600;
    color: var(--green);
  }

  .holder {
    position: absolute;
    left: 34px;
    top: 122px;
  }
  .holder-name {
    font-size: 24px;
    font-weight: 700;
    color: var(--blue);
    line-height: 1.1;
  }
  .holder-role {
    font-size: 16px;
    color: var(--green);
    margin-top: 2px;
  }

  .contact-list {
    position: absolute;
    left: 34px;
    top: 206px;
    list-style: none;
    font-size: 11.5px;
    color: var(--ink);
  }
  .contact-list li {
    display: flex;
    align-items: flex-start;
    gap: 8px;
    margin-bottom: 5px;
    line-height: 1.3;
  }
  .contact-icon {
    width: 13px;
    height: 13px;
    flex: none;
    margin-top: 1px;
  }
</style>
</head>
<body>
<main class="canvas">

  <section class="card card-front" aria-label="Business card front">
    <svg class="card-art" viewBox="0 0 560 320" preserveAspectRatio="none" aria-hidden="true">
      <path d="M0 300 L560 240 L560 320 L0 320 Z" fill="var(--blue)"/>
      <path d="M0 292 L560 232 L560 238 L0 298 Z" fill="var(--blue-deep)" opacity="0.35"/>
    </svg>
    <div class="brand">
      <span class="brand-dot"></span>
      <span class="brand-name">Torvique</span>
    </div>
    <p class="front-web">www.torvique.com</p>
  </section>

  <section class="card card-back" aria-label="Business card back">
    <svg class="card-art" viewBox="0 0 560 320" preserveAspectRatio="none" aria-hidden="true">
      <path d="M0 110 L150 70 Q175 62 200 60 L560 20 L560 0 L0 0 Z" fill="var(--card)"/>
      <path d="M0 118 L0 96 L160 58 Q185 52 210 52 L560 14 L560 34 L220 72 Q190 76 165 84 Z" fill="var(--green)"/>
      <path d="M190 52 Q200 40 230 36 L560 0 L560 22 L215 60 Q200 60 190 52 Z" fill="var(--blue)"/>
      <path d="M330 320 L560 320 L560 240 Q545 250 520 256 Z" fill="var(--blue)"/>
    </svg>

    <div class="brand">
      <span class="brand-dot"></span>
      <span class="brand-name">Torvique</span>
    </div>

    <div class="holder">
      <p class="holder-name">Prename Name</p>
      <p class="holder-role">Creative Director</p>
    </div>

    <ul class="contact-list">
      <li>
        <svg class="contact-icon" viewBox="0 0 14 14" aria-hidden="true">
          <path d="M7 1 L13 7 L11 7 L11 13 L3 13 L3 7 L1 7 Z" fill="var(--blue)"/>
        </svg>
        <span>Suite 4, 18 Harlow Street, Brenton,<br>Queensland, Australia, 4702</span>
      </li>
      <li>
        <svg class="contact-icon" viewBox="0 0 14 14" aria-hidden="true">
          <circle cx="7" cy="7" r="7" fill="var(--blue)"/>
          <path d="M4.5 3.5 L6 3.5 L6.5 5.5 L5.6 6.2 Q6.4 7.8 7.8 8.4 L8.5 7.5 L10.5 8 L10.5 9.5 Q6 10 4.5 3.5 Z" fill="#fff"/>
        </svg>
        <span>125 4870 339214</span>
      </li>
      <li>
        <svg class="contact-icon" viewBox="0 0 14 14" aria-hidden="true">
          <circle cx="7" cy="7" r="7" fill="var(--blue)"/>
          <rect x="3.5" y="4.5" width="7" height="5" fill="#fff"/>
          <path d="M3.5 4.5 L7 7.3 L10.5 4.5" fill="none" stroke="var(--blue)" stroke-width="0.8"/>
        </svg>
        <span>info@torvique.com</span>
      </li>
      <li>
        <svg class="contact-icon" viewBox="0 0 14 14" aria-hidden="true">
          <circle cx="7" cy="7" r="7" fill="var(--blue)"/>
          <circle cx="7" cy="7" r="3.6" fill="none" stroke="#fff" stroke-width="1"/>
          <path d="M3.4 7 H10.6 M7 3.4 V10.6" stroke="#fff" stroke-width="0.8"/>
        </svg>
        <span>www.torvique.com</span>
      </li>
    </ul>
  </section>

</main>
</body>
</html>
```